Brochure Design Project for Building Designer

I need a modern and edgy brochure to introduce my new business TORV Design, Commercial and Residential Building Designers.

We specialise in Building Design, Project Management and Design Consultation.

I would like the brochure to be anywhere between 2-4 pages, depending of amount of suitable content available.
Colours to be black and white with splashes of
bright colours (mostly incorporated in photos).

Main Content of brochure to be broken up into 3 (maybe 4) sections to include:

About Us
Services
Projects

Logo Text (DESIGN etc) can be changed to white if suits better with black background.

Would be nice to include sketches to give it that architectural feel.

Samples and wording will be uploaded shortly
Updates

I HAVE PROVIDED A COMPLETE UPDATE OF PROJECT REQUIREMENTS INCLUDING ALL NEW UPLOADED FILES.

PLEASE REFER TO THE BROCHURE LAYOUT PDF UPLOADEDĀ FOR FULL INFORMATION ON PROJECT INCLUDING BROCHURE LAYOUT.

IF YOU HAVE ANY QUESTIONS OR REQUIRE ANY FURTHER INFORMATION, PLEASE LET ME KNOW

I HAVE ADDED FURTHER DEVELOPED PDF DOCUMENTS OF BROCHURE.

IF YOU HAVE TROUBLE OPENING THESE DOCS IN ADOBE ILLUSTRATOR THRU ADOBE BRIDGE PLEASE LET ME KNOW & I WILL UPLOAD AI FILES.

CAN YOU PLEASE FINE TUNE GRAPHICS AND WORK ON BACKGROUND

Target Market(s)

Builders, Property Developers, Architects, Consultants, Professionals

Industry/Entity Type

Business

Requirements
Must have
• Very Professional Look
Black and White
Simple and easy to read layout
Either A4 (if only 2 pages) or
A3 double sided with centre fold (if 4 pages)
Touch up of photos (if possible) to make them stand out of the page.
Samples of recent projects with photos
Should not have
• Any comics or similar

```html
<!DOCTYPE html>
<html lang="en">
<head>
<meta charset="utf-8">
<title>TORV Design – Brochure</title>
<link rel="stylesheet" href="https://fonts.googleapis.com/css2?family=Mulish:wght@400;600&family=Jost:wght@300;400&display=swap">
<style>
:root{
  --paper:#ffffff;
  --ink:#000000;
  --panel:#050505;
  --footer-dark:#1c1c1c;
  --text:#ffffff;
  --muted:#d8d8d8;
  --accent:#e3197f;
  --plan-a:#0b0b0b;
  --plan-b:#1a1a1a;
}
*{box-sizing:border-box;margin:0;padding:0}
html,body{width:1200px;height:871px;overflow:hidden;background:var(--paper)}
body{position:relative;font-family:"Mulish",sans-serif;color:var(--text)}
.spread{position:absolute;left:11px;width:1177px;background:var(--panel)}
.spread--cover{top:11px;height:414px}
.spread--inside{top:445px;height:415px}

/* cover */
.back-cover{position:absolute;left:0;top:0;width:589px;height:414px;background:var(--ink)}
.front-cover{position:absolute;left:589px;top:0;width:588px;height:414px}
.plan-sketch{position:absolute;inset:0 0 42px 0;background:linear-gradient(135deg,var(--plan-b),var(--plan-a) 60%,#151515)}
.brand{position:absolute;font-family:"Jost",sans-serif;font-weight:300;color:var(--accent);letter-spacing:.06em;line-height:1}
.brand--large{left:266px;top:86px;font-size:64px}
.brand--small{left:274px;top:335px;font-size:24px}
.tagline{position:absolute;font-family:"Jost",sans-serif;color:var(--text);text-transform:uppercase;white-space:nowrap}
.tagline--large{left:268px;top:154px;font-size:6.6px;letter-spacing:.02em}
.tagline--small{left:275px;top:362px;font-size:3px}
.contact-bar{position:absolute;bottom:0;height:42px;display:flex;align-items:center;font-family:"Jost",sans-serif;font-size:11px;white-space:nowrap;overflow:hidden}
.back-cover .contact-bar{left:0;width:589px;padding-left:13px}
.front-cover .contact-bar{left:0;width:588px;padding-left:12px;background:var(--footer-dark)}
.contact-bar .sep{margin:0 6px}

/* inside */
.photo{position:absolute}
.photo--interior{left:15px;top:17px;width:246px;height:382px;background:linear-gradient(160deg,#efe0b8,#c9a566 45%,#3a2a1a)}
.photo--pool{left:610px;top:208px;width:268px;height:191px;background:linear-gradient(170deg,#6b5a34,#c2a35a 40%,#1f4a3a 75%,#0d2a22)}
.photo--p1{left:883px;top:17px;width:139px;height:122px;background:linear-gradient(180deg,#4c83c9,#b4c4d0 55%,#7e7a76)}
.photo--p2{left:1025px;top:17px;width:138px;height:122px;background:linear-gradient(180deg,#6fa1da,#e2e2e2 50%,#6a6a6a)}
.photo--p3{left:883px;top:145px;width:139px;height:124px;background:linear-gradient(180deg,#3f73c4,#e8ded2 50%,#3fa8a8)}
.photo--p4{left:1025px;top:145px;width:138px;height:124px;background:linear-gradient(180deg,#3d7ad0,#f0f2f4 55%,#6aa048)}
.photo--p5{left:883px;top:274px;width:139px;height:125px;background:linear-gradient(160deg,#e8eef0,#a9c8c6 50%,#3a4a3c)}
.photo--p6{left:1025px;top:274px;width:138px;height:125px;background:linear-gradient(160deg,#e6c98a,#9c6a3c 55%,#3a2618)}

.section{position:absolute}
.section--about{left:288px;top:30px;width:290px}
.section--services{left:288px;top:171px;width:300px}
.section--projects{left:610px;top:30px;width:270px}
.section h2{font-family:"Jost",sans-serif;font-weight:400;font-size:18px;letter-spacing:.01em;line-height:1;margin-bottom:8px}
.lead{font-family:"Jost",sans-serif;text-transform:uppercase;font-size:10px;line-height:1.25;margin-bottom:12px}
.body-copy{font-size:7.4px;line-height:1.42;color:var(--muted);margin-bottom:9px}
.bullets{list-style:none}
.bullets li{position:relative;padding-left:11px;font-family:"Jost",sans-serif;font-size:8px;text-transform:uppercase;line-height:1;margin-bottom:9.3px}
.bullets li::before{content:"";position:absolute;left:0;top:1px;width:5px;height:5px;border-radius:50%;background:var(--accent)}
.section--projects .bullets li{margin-bottom:8.3px}
</style>
</head>
<body>

<section class="spread spread--cover">
  <div class="back-cover">
    <div class="brand brand--small">TORV</div>
    <div class="tagline tagline--small">Commercial + Residential Building Designers</div>
    <div class="contact-bar">PO BOX 418 NORTHBRIDGE WA 6865<span class="sep">|</span>studio@torvdesign.com.au<span class="sep">|</span>0400 123 987<span class="sep">|</span>www.torvdesign.com.au</div>
  </div>
  <div class="front-cover">
    <div class="plan-sketch" role="img" aria-label="White line architectural floor plan of a gallery and cafe on black"></div>
    <div class="brand brand--large">TORV</div>
    <div class="tagline tagline--large">Commercial + Residential Building Designers</div>
    <div class="contact-bar">PO BOX 418 NORTHBRIDGE WA 6865<span class="sep">|</span>studio@torvdesign.com.au<span class="sep">|</span>0400 123 987<span class="sep">|</span>www.torvdesign.com.au</div>
  </div>
</section>

<section class="spread spread--inside">
  <div class="photo photo--interior" role="img" aria-label="Double-height living and dining interior with a floating staircase"></div>

  <div class="section section--about">
    <h2>ABOUT US</h2>
    <p class="body-copy">Lorem ipsum dolor sit amet, consectetur adipiscing elit. Nulla lobortis consequat mauris, eget eleifend nunc viverra viverra. Ut ac risus odio. Aliquam pretium purus sed nulla feugiat blandit.</p>
    <p class="body-copy">Cras vel libero ut lacus eleifend tempor. Phasellus eleifend, magna non tincidunt accumsan, justo arcu cursus ipsum, non porttitor sapien quam vel magna. Maecenas elit nisl, molestie nec dapibus nec, aliquet a erat. Donec scelerisque lacus a libero suscipit auctor volutpat enim euismod. Mauris porta, lacus ut ullamcorper sodales, mauris tortor feugiat purus, nec aliquam neque purus ac metus.</p>
  </div>

  <div class="section section--services">
    <h2>SERVICES</h2>
    <p class="lead">We are able to provide a wide range of services<br>including the following:</p>
    <ul class="bullets">
      <li>Project planning</li>
      <li>Design concepts</li>
      <li>Design development / development approval</li>
      <li>Consultant liaison + management</li>
      <li>Building certification</li>
      <li>Tenderi construction documentation</li>
      <li>Project management</li>
      <li>3D modelling &amp; renders</li>
      <li>Re-documentation &amp; design consultation</li>
      <li>Drafting services</li>
    </ul>
  </div>

  <div class="section section--projects">
    <h2>OUR PROJECTS</h2>
    <p class="lead">Lorem ipsum dolor sit amet, consectetur adipi<br>scing elit. Nulla lobortis consequat mauris</p>
    <ul class="bullets">
      <li>Integer eget ligula lectus, eget pulvinar diam.</li>
      <li>Donec porttitor viverra nibh ac pulvinar.</li>
      <li>Pellentesque habitant morbi tristique</li>
      <li>Senectus et netus et malesuada fames ac</li>
      <li>Turpis egestas. Phasellus mollis pharetra dignissim.</li>
      <li>Ut pretium blandit lectus congue fringilla.</li>
      <li>Aliquam imperdiet ante quis odio congue ultrices.</li>
    </ul>
  </div>

  <div class="photo photo--pool" role="img" aria-label="Home at dusk with lit living room opening onto a pool"></div>
  <div class="photo photo--p1" role="img" aria-label="Single-storey commercial building under blue sky"></div>
  <div class="photo photo--p2" role="img" aria-label="Multi-storey office building on a street corner"></div>
  <div class="photo photo--p3" role="img" aria-label="Apartment block beside a swimming pool"></div>
  <div class="photo photo--p4" role="img" aria-label="White modern house with palm trees"></div>
  <div class="photo photo--p5" role="img" aria-label="Bright kitchen and dining interior"></div>
  <div class="photo photo--p6" role="img" aria-label="Warm-toned bedroom interior"></div>
</section>

</body>
</html>
```